Business Card Design Project

I am a property development company requiring a professional looking business card.
The name of the my company is PLW CANOPIES. I have attached a couple of designs that I have created on my own, that can give you an idea of what I am after.
Above the wording PLW CANOPIES, I have a orange arc above these words to signify the sun is begining to rise above the horizon.
I have a few designs; Middle Rays, Side Rays, Horizontals Rays which are OK, but I am looking for the better design.
The Rear design of the card is what I had came up with. If you have a better design, I am happy to see it.
The design of the card can follow what I have came up with, or it can be totally different. The fonts needs to be adjusted to another font that is more suitable.
The colours that I have used is what I think I would like to stick with. As I have mentioned, the orange arc is to signify the sun rising. If you have a better colour scheme, I would consider it.
Looking at dealing with first home buyers and proffesional people.
Business

```html
<!DOCTYPE html>
<html lang="en">
<head>
<meta charset="utf-8">
<title>PLW Canopies – Business Card Concepts</title>
<link rel="stylesheet" href="https://fonts.googleapis.com/css2?family=Open+Sans:wght@400;600;700&display=swap">
<style>
  :root {
    --page: #ffffff;
    --ink: #231f1c;
    --edge: #2b2b2b;
    --white: #ffffff;
    --cream: #fdf7dc;
    --cream-warm: #fbe6b0;
    --peach: #f6b35c;
    --orange: #ee7d1d;
    --sun-red: #e2231a;
    --red: #d62a2c;
    --red-deep: #961c24;
    --blue: #0f86c9;
    --sky: #2bb7e8;
    --yellow: #fbcb0a;
    --amber: #f29a12;
    --green: #a9c81c;
  }
  * { box-sizing: border-box; margin: 0; padding: 0; }
  html, body {
    width: 1200px; height: 1145px; overflow: hidden;
    background: var(--page);
    font-family: "Open Sans", Arial, sans-serif;
  }
  .sheet { position: relative; width: 1200px; height: 1145px; }

  .card {
    position: absolute;
    width: 497px; height: 306px;
    border: 1.5px solid var(--edge);
    border-radius: 28px;
    overflow: hidden;
    color: var(--ink);
    text-align: center;
  }
  .card--left { left: 85px; }
  .card--right { left: 611px; }
  .card--row1 { top: 82px; }
  .card--row2 { top: 416px; }
  .card--row3 { top: 750px; }

  .card__backdrop { position: absolute; inset: 0; }
  .card--middle-rays .card__backdrop {
    background:
      radial-gradient(ellipse 45% 70% at 50% 100%, var(--sun-red) 0%, rgba(226,35,26,0) 100%),
      linear-gradient(to bottom, var(--cream) 0%, var(--cream-warm) 38%, var(--peach) 62%, var(--orange) 100%);
  }
  .card--side-rays .card__backdrop {
    background:
      radial-gradient(ellipse 30% 55% at 50% 100%, var(--sun-red) 0%, rgba(226,35,26,0) 100%),
      linear-gradient(to bottom, var(--cream) 0%, var(--cream) 45%, var(--peach) 62%, var(--orange) 100%);
  }
  .card--soft-rays .card__backdrop {
    background:
      radial-gradient(ellipse 20% 60% at 50% 100%, var(--sun-red) 0%, rgba(226,35,26,0) 100%),
      linear-gradient(to bottom, var(--cream) 0%, var(--cream-warm) 40%, var(--peach) 70%, var(--orange) 100%);
  }
  .card--red-burst { color: var(--white); }
  .card--red-burst .card__backdrop {
    background: radial-gradient(ellipse 75% 80% at 50% 40%, var(--red) 0%, #c92229 55%, var(--red-deep) 100%);
  }
  .card--horizon-bands { color: var(--white); }
  .card--horizon-bands .card__backdrop {
    background: linear-gradient(to bottom, var(--blue) 0%, var(--sky) 30%, var(--yellow) 45%, var(--amber) 62%, var(--yellow) 78%, var(--green) 100%);
  }
  .card--golden-diamonds .card__backdrop {
    background: linear-gradient(160deg, var(--yellow) 0%, #f8b90c 50%, var(--amber) 100%);
  }

  .card__line {
    position: absolute; left: 0; right: 0;
    top: var(--y);
    transform: translateY(-50%);
    white-space: nowrap;
    line-height: 1.2;
  }
  .brand-name { font-size: 40px; font-weight: 400; letter-spacing: 0.5px; }
  .brand-tagline { font-size: 17px; font-weight: 400; }
  .person-name { font-size: 21px; font-weight: 700; }
  .person-role { font-size: 18px; font-weight: 700; }
  .contact { font-size: 15px; font-weight: 700; }
  .card--red-burst .contact { font-size: 14px; }
</style>
</head>
<body>
<main class="sheet">

  <section class="card card--left card--row1 card--middle-rays">
    <div class="card__backdrop" role="img" aria-label="Sunrise rays fanning up from the bottom centre in cream, orange and red"></div>
    <div class="card__line brand-name" style="--y:73px">PLW CANOPIES</div>
    <div class="card__line brand-tagline" style="--y:106px">Property Developments</div>
    <div class="card__line person-name" style="--y:141px">Marcus Leed</div>
    <div class="card__line person-role" style="--y:168px">Director</div>
    <div class="card__line contact" style="--y:223px">27 Alder Street Kirrawee NSW 2232 Australia</div>
    <div class="card__line contact" style="--y:242px">0400 555 123</div>
    <div class="card__line contact" style="--y:261px">marcus@plwcanopies.com.au</div>
    <div class="card__line contact" style="--y:281px">www.plwcanopies.com.au</div>
  </section>

  <section class="card card--right card--row1 card--side-rays">
    <div class="card__backdrop" role="img" aria-label="Sunrise rays spreading sideways from the bottom centre in cream, orange and red"></div>
    <div class="card__line brand-name" style="--y:73px">PLW CANOPIES</div>
    <div class="card__line brand-tagline" style="--y:106px">Property Developments</div>
    <div class="card__line person-name" style="--y:141px">Marcus Leed</div>
    <div class="card__line person-role" style="--y:168px">Director</div>
    <div class="card__line contact" style="--y:223px">27 Alder Street Kirrawee NSW 2232 Australia</div>
    <div class="card__line contact" style="--y:242px">0400 555 123</div>
    <div class="card__line contact" style="--y:261px">marcus@plwcanopies.com.au</div>
    <div class="card__line contact" style="--y:281px">www.plwcanopies.com.au</div>
  </section>

  <section class="card card--left card--row2 card--soft-rays">
    <div class="card__backdrop" role="img" aria-label="Soft sunrise rays in pale yellow fading to orange with a red centre"></div>
    <div class="card__line brand-name" style="--y:72px">PLW CANOPIES</div>
    <div class="card__line brand-tagline" style="--y:106px">Property Developments</div>
    <div class="card__line person-name" style="--y:160px">Marcus Leed</div>
    <div class="card__line person-role" style="--y:186px">Director</div>
    <div class="card__line contact" style="--y:223px">27 Alder Street Kirrawee NSW 2232 Australia</div>
    <div class="card__line contact" style="--y:242px">0400 555 123</div>
    <div class="card__line contact" style="--y:261px">marcus@plwcanopies.com.au</div>
    <div class="card__line contact" style="--y:281px">www.plwcanopies.com.au</div>
  </section>

  <section class="card card--right card--row2 card--red-burst">
    <div class="card__backdrop" role="img" aria-label="Red starburst rays radiating from the centre"></div>
    <div class="card__line brand-name" style="--y:89px">PLW CANOPIES</div>
    <div class="card__line brand-tagline" style="--y:123px">Property Developments</div>
    <div class="card__line person-name" style="--y:162px">Marcus Leed</div>
    <div class="card__line person-role" style="--y:189px">Director</div>
    <div class="card__line contact" style="--y:217px">27 Alder Street Kirrawee NSW 2232 Australia</div>
    <div class="card__line contact" style="--y:237px">0400 555 123</div>
    <div class="card__line contact" style="--y:257px">marcus@plwcanopies.com.au</div>
    <div class="card__line contact" style="--y:277px">www.plwcanopies.com.au</div>
  </section>

  <section class="card card--left card--row3 card--horizon-bands">
    <div class="card__backdrop" role="img" aria-label="Horizontal rays meeting at a horizon point in blue, yellow, orange and green"></div>
    <div class="card__line brand-name" style="--y:73px">PLW CANOPIES</div>
    <div class="card__line brand-tagline" style="--y:102px">Property Developments</div>
    <div class="card__line person-name" style="--y:131px">Marcus Leed – Director</div>
    <div class="card__line contact" style="--y:206px">0400 555 123</div>
    <div class="card__line contact" style="--y:225px">marcus@plwcanopies.com.au</div>
    <div class="card__line contact" style="--y:245px">www.plwcanopies.com.au</div>
    <div class="card__line contact" style="--y:265px">27 Alder Street Kirrawee NSW 2232 Australia</div>
  </section>

  <section class="card card--right card--row3 card--golden-diamonds">
    <div class="card__backdrop" role="img" aria-label="Diamond lattice pattern in golden yellow and orange"></div>
    <div class="card__line brand-name" style="--y:73px">PLW CANOPIES</div>
    <div class="card__line brand-tagline" style="--y:106px">Property Developments</div>
    <div class="card__line person-name" style="--y:151px">Marcus Leed</div>
    <div class="card__line person-role" style="--y:178px">Director</div>
    <div class="card__line contact" style="--y:223px">27 Alder Street Kirrawee NSW 2232 Australia</div>
    <div class="card__line contact" style="--y:243px">0400 555 123</div>
    <div class="card__line contact" style="--y:262px">marcus@plwcanopies.com.au</div>
    <div class="card__line contact" style="--y:282px">www.plwcanopies.com.au</div>
  </section>

</main>
</body>
</html>
```